Project Quarter 2

A business card with the following details

Rob Kettering
Consultant/Speaker/Trainer

The Brand Quarter Hub (Insert Logo)
Fresh Thinking for Brand Builders
www.brandquarterhub.com

Rob.Kettering@brandquarterhub.com
+61 452 918 604
Facebook icon
Twitter icon
Linkedin icon
Google+ icon
Pinterist icon

Target Market(s)

Small and Medium sized business owners
Brand marketers

Industry/Entity Type

Business

Requirements
Must have
• Utilise The Brand Quarter Hub Logo and colour scheme
Nice to have
• More male than female in outlook.
Have a connnected feel to it and a link to a precinct good too.
Bold and simple design the ideal

```html
<!DOCTYPE html>
<html lang="en">
<head>
<meta charset="utf-8">
<title>The Brand Quarter Hub – Business Card</title>
<link rel="stylesheet" href="https://fonts.googleapis.com/css2?family=Cabin:wght@400;500&display=swap">
<style>
  :root {
    --page-bg: #e9ecee;
    --card-blue: #1f4d6e;
    --card-blue-deep: #163b57;
    --card-blue-light: #2a5f84;
    --accent-teal: #6cc4d3;
    --text-light: #dfeaf0;
    --text-soft: #9fc3d3;
    --shadow: rgba(18, 40, 58, 0.28);
  }
  * { box-sizing: border-box; margin: 0; padding: 0; }
  html, body {
    width: 1200px;
    height: 900px;
    overflow: hidden;
  }
  body {
    background: var(--page-bg);
    font-family: "Cabin", "Gill Sans", sans-serif;
    display: flex;
    flex-direction: column;
    align-items: center;
    justify-content: center;
    gap: 56px;
  }
  .card {
    width: 540px;
    height: 330px;
    border-radius: 4px;
    box-shadow: 0 14px 34px var(--shadow);
    position: relative;
    overflow: hidden;
  }
  .card--back {
    background: radial-gradient(ellipse at 45% 42%, var(--card-blue-light) 0%, var(--card-blue) 45%, var(--card-blue-deep) 100%);
    display: flex;
    flex-direction: column;
    align-items: center;
    justify-content: center;
  }
  .card--front {
    background: linear-gradient(160deg, var(--card-blue-light) 0%, var(--card-blue) 55%, var(--card-blue-deep) 100%);
  }
  .brand-name {
    font-weight: 400;
    color: var(--text-light);
    white-space: nowrap;
  }
  .card--back .brand-name { font-size: 36px; }
  .tagline {
    margin-top: 40px;
    font-size: 15px;
    color: var(--text-soft);
    letter-spacing: 0.3px;
  }
  .front-layout {
    position: absolute;
    left: 150px;
    top: 60px;
  }
  .card--front .brand-name { font-size: 26px; }
  .contact { margin-top: 18px; }
  .contact__name {
    font-size: 23px;
    font-weight: 400;
    text-transform: uppercase;
    letter-spacing: 1px;
    color: var(--accent-teal);
  }
  .contact__role {
    font-size: 15px;
    color: var(--text-light);
    margin-top: 2px;
  }
  .contact__lines {
    list-style: none;
    margin-top: 14px;
    font-size: 13px;
    line-height: 1.5;
    color: var(--text-light);
  }
  .social-row {
    display: flex;
    gap: 6px;
    margin-top: 12px;
  }
  .social-row__item {
    width: 14px;
    height: 14px;
    border-radius: 2px;
    background: var(--accent-teal);
  }
</style>
</head>
<body>
  <section class="card card--back" aria-label="Card back">
    <p class="brand-name">The Brand Quarter Hub</p>
    <p class="tagline">Fresh Thinking for Brand Builders</p>
  </section>

  <section class="card card--front" aria-label="Card front">
    <div class="front-layout">
      <p class="brand-name">The Brand Quarter Hub</p>
      <div class="contact">
        <h1 class="contact__name">Rob Kettering</h1>
        <p class="contact__role">Consultant/Speaker/Trainer</p>
        <ul class="contact__lines">
          <li>+61 452 918 604</li>
          <li>Rob.Kettering@brandquarterhub.com</li>
          <li>www.brandquarterhub.com</li>
        </ul>
        <div class="social-row" aria-label="Social profiles">
          <span class="social-row__item"></span>
          <span class="social-row__item"></span>
          <span class="social-row__item"></span>
          <span class="social-row__item"></span>
          <span class="social-row__item"></span>
        </div>
      </div>
    </div>
  </section>
</body>
</html>
```